Easy one-page Web Design with ready made sketch/template

This project have an already made one page Web Design sketch/template that should be used as a base. It needs professional touch and improvements but should be quite straight forward for you to make.

Webpage: Offers local graphical design services

Attached following documents for you:
- PSD sketch
- JPG sketch
- Word file with project description (read carefully)
- Logo

Reason: Project extended to get the final designs submitted. Thanks

Target Market(s)

Logo design

Industry/Entity Type

Graphic Design

Number of Pages Required

1 page

Requirements
Must have
• Please refer to attached word document.
Nice to have
Should not have

```html
<!DOCTYPE html>
<html lang="sv">
<head>
<meta charset="utf-8">
<title>Markverket – Logo design</title>
<link rel="stylesheet" href="https://fonts.googleapis.com/css2?family=Montserrat:wght@300;400;500;600;700;800&display=swap">
<style>
:root{
  --ink:#2b2b2b;
  --muted:#555;
  --blue:#4a80bc;
  --blue-dark:#2f5f9a;
  --orange:#ee7d22;
  --orange-btn:#f26a2b;
  --red:#c0261f;
  --yellow:#f6b83a;
  --green:#2e7d20;
  --header:#f7f7f7;
  --line:#e9ddd0;
  --card-border:#cfcfcf;
  --card-top:#f6f6f6;
}
*{box-sizing:border-box;margin:0;padding:0}
html,body{width:1200px;height:1200px;overflow:hidden;background:#fff;font-family:"Montserrat",sans-serif;color:var(--ink)}
.page{position:relative;width:1200px;height:1200px;overflow:hidden}

.site-header{position:absolute;left:0;top:0;width:1200px;height:71px;background:var(--header)}
.brand{position:absolute;left:119px;top:18px;display:flex;align-items:center;gap:8px;font-weight:600;font-size:22px;color:var(--blue)}
.brand-mark{width:14px;height:14px;background:var(--blue)}
.nav a{position:absolute;top:29px;font-size:11px;font-weight:600;color:#333;text-decoration:none;letter-spacing:.2px}
.order-btn{position:absolute;left:808px;top:19px;width:121px;height:34px;border-radius:5px;background:var(--orange-btn);color:#fff;font-size:11px;font-weight:700;display:flex;align-items:center;justify-content:center;gap:7px}
.call{position:absolute;left:962px;top:30px;font-size:11px;font-weight:600;color:#333}

.hero{position:absolute;left:0;top:71px;width:1200px;height:475px;
  background:linear-gradient(160deg,#e6e6e6 0%,#f2f2f2 35%,#c9d3df 55%,#3b6ea8 75%,#e0e0e0 100%)}
.how-btn{position:absolute;left:521px;top:310px;width:162px;height:28px;border-radius:14px;background:var(--orange-btn);color:#fff;font-size:11px;font-weight:700;display:flex;align-items:center;gap:14px;padding-left:12px}
.start{position:absolute;left:0;width:1200px;top:396px;text-align:center;font-size:16px;font-weight:800;color:#fff}
.start span{color:var(--red)}

.feature{position:absolute;top:558px;width:240px;text-align:center}
.feature svg{display:block;margin:0 auto}
.feature p{margin-top:16px;font-size:11px;font-weight:600;color:#222}
.divider{position:absolute;left:0;top:735px;width:1200px;height:3px;border-top:1px solid var(--line);border-bottom:1px solid var(--line)}

.section-title{position:absolute;left:0;top:772px;width:1200px;text-align:center;font-size:22px;font-weight:700;color:#555}
.section-sub{position:absolute;left:0;top:804px;width:1200px;text-align:center;font-size:14px;font-weight:700;color:var(--blue)}

.tier{position:absolute;width:228px;text-align:center}
.tier-name{font-size:15px;font-weight:400;color:#444;height:21px}
.card{margin-top:20px;border:1px solid var(--card-border);border-radius:6px 6px 0 0;height:400px;background:#fff;overflow:hidden}
.price{height:58px;background:var(--card-top);padding-top:6px}
.price b{font-size:22px;font-weight:700;color:#333}
.price small{font-size:12px}
.price .note{font-size:14px;font-weight:300;color:#333;margin-top:-3px}
.select{height:48px;background:var(--blue);color:#fff;font-size:21px;font-weight:400;display:flex;align-items:center;justify-content:center}
.select.recommended{background:var(--orange)}
.features{list-style:none;padding-top:18px;font-size:14px;line-height:19.3px;color:#333;font-weight:400}
</style>
</head>
<body>
<div class="page">
  <header class="site-header">
    <div class="brand"><span class="brand-mark"></span>Markverket</div>
    <nav class="nav">
      <a style="left:477px">PRODUCTS</a>
      <a style="left:565px">GALLERY</a>
      <a style="left:650px">FAQ</a>
      <a style="left:706px">CONTACT US</a>
    </nav>
    <div class="order-btn">
      <svg width="13" height="12" viewBox="0 0 13 12"><path d="M0 1h2l2 6h7l1.5-4.5H3.5" fill="none" stroke="#fff" stroke-width="1.6"/><circle cx="5" cy="10" r="1.2" fill="#fff"/><circle cx="10" cy="10" r="1.2" fill="#fff"/></svg>
      ORDER LOGO
    </div>
    <div class="call">CALL US 08-555 0142</div>
  </header>

  <section class="hero" role="img" aria-label="3D rendering of rows of blue and white cubes">
    <div class="how-btn">
      <svg width="20" height="20" viewBox="0 0 20 20"><circle cx="10" cy="10" r="10" fill="#fff"/><path d="M8 6l6 4-6 4z" fill="var(--orange-btn)"/></svg>
      HOW IT WORKS?
    </div>
    <div class="start">START FROM <span>$1495</span></div>
  </section>

  <div class="feature" style="left:160px">
    <svg width="120" height="120" viewBox="0 0 120 120">
      <path d="M32 108.5A56 56 0 1 1 88 108.5" fill="none" stroke="var(--yellow)" stroke-width="2"/>
      <g fill="none" stroke="#222" stroke-width="1.5">
        <path d="M60 44l4 9 9 1-7 6 2 9-8-5-8 5 2-9-7-6 9-1z"/>
        <path d="M42 62l2.5 5 5.5.5-4 4 1 5.5-5-3-5 3 1-5.5-4-4 5.5-.5z"/>
        <path d="M78 62l2.5 5 5.5.5-4 4 1 5.5-5-3-5 3 1-5.5-4-4 5.5-.5z"/>
        <path d="M60 32v7M47 36l4 6M73 36l-4 6M40 45l6 3M80 45l-6 3"/>
      </g>
    </svg>
    <p>100% SATISFACTION GUARANTEE</p>
  </div>
  <div class="feature" style="left:481px">
    <svg width="120" height="120" viewBox="0 0 120 120">
      <path d="M32 108.5A56 56 0 1 1 88 108.5" fill="none" stroke="var(--blue-dark)" stroke-width="2"/>
      <g fill="none" stroke="#222" stroke-width="2">
        <rect x="27" y="40" width="38" height="33" rx="3"/>
        <path d="M65 52h12l8 10v11H65z"/>
        <circle cx="37" cy="76" r="5" fill="#fff"/><circle cx="75" cy="76" r="5" fill="#fff"/>
        <circle cx="41" cy="54" r="9"/><path d="M41 49v5h4"/>
      </g>
    </svg>
    <p>DELIVERY WITHING 24-HOURS</p>
  </div>
  <div class="feature" style="left:801px">
    <svg width="120" height="120" viewBox="0 0 120 120">
      <path d="M32 108.5A56 56 0 1 1 88 108.5" fill="none" stroke="var(--green)" stroke-width="2"/>
      <g fill="none" stroke="#222" stroke-width="1.5">
        <rect x="57" y="35" width="28" height="20" rx="2"/>
        <path d="M62 42h14M62 47h18M62 52h10"/>
        <circle cx="47" cy="66" r="9"/><circle cx="47" cy="66" r="5"/>
        <path d="M42 74v8l5-3 5 3v-8"/>
      </g>
    </svg>
    <p>9/10 RATING ON RATENEST</p>
  </div>

  <div class="divider"></div>

  <h2 class="section-title">SELECT A PACKAGE</h2>
  <p class="section-sub">FIXED PRICE!</p>

  <div class="tier" style="left:119px;top:908px">
    <div class="tier-name">starter</div>
    <div class="card">
      <div class="price"><b>1495</b><small>,-</small><div class="note">+moms</div></div>
      <div class="select">select</div>
      <ul class="features"><li>3 logotyputkast</li><li>1 ändring/revision</li><li>Filer för webben</li></ul>
    </div>
  </div>

  <div class="tier" style="left:363px;top:908px">
    <div class="tier-name">silver</div>
    <div class="card">
      <div class="price"><b>2495</b><small>,-</small><div class="note">+moms</div></div>
      <div class="select">select</div>
      <ul class="features"><li>6 logotyputkast</li><li>3 ändringar/revisioner</li><li>Filer för webben</li><li>Vektorgrafiska filer för tryck</li></ul>
    </div>
  </div>

  <div class="tier" style="left:608px;top:868px">
    <div class="tier-name">unlimited</div>
    <div class="card">
      <div class="price"><b>3995</b><small>,-</small><div class="note">/ord. pris 6995,-</div></div>
      <div class="select recommended">recommended</div>
      <ul class="features"><li>100% nöjdhetsgaranti</li><li>10 logotyputkast</li><li>Obergränsat med</li><li>ändringar/revisioner</li><li>Allt du behöver ingår</li><li>Visitkort design</li><li>Brevpapper design</li><li>Logotypguide</li><li>Telefonsupport</li><li>Social logotyp</li></ul>
    </div>
  </div>

  <div class="tier" style="left:852px;top:908px">
    <div class="tier-name">platinum</div>
    <div class="card">
      <div class="price"><b>9995</b><small>,-</small><div class="note">+moms</div></div>
      <div class="select">select</div>
      <ul class="features"><li>Allt i Unlimited paketet</li><li>Proffsig hemsida som</li><li>enkelt uppdaterar</li><li>Responsiv Design</li><li>(för mobiler och läsplattor)</li><li>490kr/mån (ingen</li><li>bindningstid)</li><li>1-tim support per månad</li></ul>
    </div>
  </div>
</div>
</body>
</html>
```